Brightpath Dental Studio

Please go to www.brightpathdentalstudio.example and obtain the current company logo.
Doctors name are
Marita Velbonne, DDS
Denis Kalb, DMD
Addresses are
318 Larchmont Ave
Teaneck, NJ 07666
201-555-0147
And
872 14th St.
West New York, NJ 07093
201-555-0182
Theme of the business card should feel modrrn and similar to the website.
Front side should include company logo, doctors name, addresses, phone numbers.
Back of the card should include blank lines for patient's name. Date and time for next scheduled appointment. And notice of 24-hr cancellation courtesy policy.
Dental

```html
<!DOCTYPE html>
<html lang="en">
<head>
<meta charset="UTF-8">
<title>Brightpath Dental Studio – Appointment Card</title>
<link rel="stylesheet" href="https://fonts.googleapis.com/css2?family=Figtree:wght@400;700&display=swap">
<style>
  :root {
    --navy: #141a46;
    --orange: #f7891f;
    --white: #ffffff;
  }
  html, body {
    margin: 0;
    padding: 0;
    width: 1200px;
    height: 686px;
    overflow: hidden;
    background: var(--white);
  }
  .card {
    position: relative;
    width: 1200px;
    height: 686px;
    background: var(--white);
    font-family: "Figtree", "Avenir Next", sans-serif;
    color: var(--navy);
  }
  .patient-name-field {
    position: absolute;
    left: 87px;
    top: 140px;
    width: 1024px;
    height: 100px;
    box-sizing: border-box;
    border: 4.5px solid var(--navy);
    border-radius: 50px;
  }
  .section-title {
    position: absolute;
    left: 95px;
    top: 316px;
    margin: 0;
    font-size: 34px;
    font-weight: 700;
    letter-spacing: 0.2px;
    color: var(--orange);
    line-height: 1;
  }
  .section-rule {
    position: absolute;
    left: 95px;
    top: 372px;
    width: 1008px;
    height: 4.5px;
    background: var(--navy);
  }
  .field-icons {
    position: absolute;
    left: 0;
    top: 0;
    width: 1200px;
    height: 686px;
  }
  .policy-band {
    position: absolute;
    left: 0;
    bottom: 0;
    width: 1200px;
    height: 99px;
    background: var(--navy);
    display: flex;
    align-items: center;
    justify-content: center;
  }
  .policy-note {
    margin: 0;
    font-size: 35px;
    font-weight: 400;
    color: var(--white);
    letter-spacing: 0.1px;
  }
</style>
</head>
<body>
  <main class="card">
    <div class="patient-name-field" aria-label="Patient name"></div>

    <h2 class="section-title">NEXT APPOINTMENT</h2>
    <div class="section-rule"></div>

    <svg class="field-icons" viewBox="0 0 1200 686" aria-hidden="true">
      <!-- calendar icon -->
      <g class="icon-date" fill="var(--navy)">
        <rect x="97" y="444" width="55" height="48" fill="none" stroke="var(--navy)" stroke-width="5"/>
        <rect x="97" y="444" width="55" height="12"/>
        <rect x="106" y="436" width="6" height="14"/>
        <rect x="137" y="436" width="6" height="14"/>
      </g>
      <!-- date separators -->
      <g class="date-separators" stroke="var(--navy)" stroke-width="2.5">
        <line x1="291" y1="455" x2="278" y2="486"/>
        <line x1="414" y1="455" x2="401" y2="486"/>
      </g>
      <!-- clock icon -->
      <g class="icon-time" fill="none" stroke="var(--navy)" stroke-width="5">
        <circle cx="638" cy="463" r="27"/>
        <polyline points="636,446 636,467 652,467" stroke-linecap="square"/>
      </g>
    </svg>

    <footer class="policy-band">
      <p class="policy-note">A full 24 hours notice is required for cancelling appointments</p>
    </footer>
  </main>
</body>
</html>
```